Raised Fingerprint Business Card Design

I need a business card design and I would like the image for the business cards to carry on to my stationary and website. My business is Forensic Consulting. I will be providing services to prosecuting and defense attorneys as well as law enforcement agencies in the areas of latent print comparison, crime scene investigations, and forensic training. I am looking for a color scheme of red, black, and silver. I would like a fingerprint that is raised and the text to be raised to some degree depending on your recommendations. with a fingerprint glass. I would like the card to include the business name, my name the deignation CLPE after it, phone number, web address, and physical address. I would like the phrase "veritas aequitas " placed discretely at the bottome of the card-subtle/not too bold.

Target Market(s)

Attorneys and law enforcement agencies

Industry/Entity Type

Business

Contact Information for Business Card

Delia Forsythe, CLPE
Brightwell Evidence Group, LLC
P.O. Box 583172 Sacramento, CA 95817
916.428.3071
www.brightwellevidencegroup.example
brightwellevidence@mailbox.example

Colors
ec1f27

Requirements
Must have
• Fingerprint and old fashioned handheld magnifying glass (Sherlock Holmes style.
• The Latin phrase listed above placed at the bottom of the front of the card discreetly.
Nice to have
• The fingerprint ridges (black lines) raised so the customer can feel it the texture.
• Raised lettering for either my name or the company name.
Should not have
• None that I can think of now.

```html
<!DOCTYPE html>
<html lang="en">
<head>
<meta charset="utf-8">
<title>Brightwell Evidence Group — Business Cards</title>
<link href="https://fonts.googleapis.com/css2?family=Open+Sans:wght@400;600&display=swap" rel="stylesheet">
<style>
  :root {
    --stage: #2f2f31;
    --card: #f4f4f4;
    --card-edge: #dcdcdc;
    --red: #d51f26;
    --ink: #1c1c1c;
    --muted: #a3a7ab;
    --white: #ffffff;
    --silver-a: #e9ecee;
    --silver-b: #9aa3aa;
  }
  * { box-sizing: border-box; margin: 0; padding: 0; }
  html, body { width: 1200px; height: 1000px; overflow: hidden; }
  body {
    background: var(--stage);
    font-family: "Open Sans", Arial, sans-serif;
    display: flex; flex-direction: column; align-items: center; justify-content: center; gap: 56px;
  }
  .card {
    position: relative; width: 700px; height: 400px;
    background: radial-gradient(ellipse at 40% 40%, var(--white), var(--card) 60%, var(--card-edge));
    border-radius: 28px; overflow: hidden;
    box-shadow: 0 18px 40px rgba(0,0,0,.45);
  }
  .emblem-area {
    position: absolute; width: 210px; height: 140px; border-radius: 50%;
    background: radial-gradient(ellipse, var(--silver-b), var(--silver-a) 70%, transparent 72%);
  }
  .company { font-size: 26px; color: var(--red); font-weight: 400; line-height: 1.2; }

  /* Front card */
  .card--brand .emblem-area { left: 190px; top: 95px; }
  .card--brand .company { position: absolute; left: 48px; top: 290px; }
  .motto {
    position: absolute; left: 0; width: 520px; bottom: 24px;
    text-align: center; font-size: 12px; letter-spacing: 3px;
    color: var(--muted); font-style: italic;
  }
  .side-strip {
    position: absolute; right: 0; top: 0; width: 180px; height: 100%;
    background: var(--red); display: flex; flex-direction: column;
  }
  .side-strip span { flex: 1; border-bottom: 2px solid var(--white); }
  .side-strip span:last-child { border-bottom: none; }

  /* Contact card */
  .card--contact .emblem-area { left: 70px; top: 90px; }
  .card--contact .company { position: absolute; left: 80px; top: 245px; }
  .holder { position: absolute; left: 380px; top: 40px; }
  .holder-name { color: var(--red); font-size: 23px; line-height: 1.2; }
  .holder-title { color: var(--ink); font-size: 14px; font-weight: 600; }
  .contact-panel {
    position: absolute; right: 0; top: 112px; width: 370px; height: 232px;
    background: var(--red); color: var(--white);
    padding: 24px 20px; list-style: none; font-size: 15px;
    display: flex; flex-direction: column; gap: 12px;
  }
  .contact-panel li { display: flex; gap: 12px; align-items: flex-start; line-height: 1.3; }
  .contact-panel svg { flex: none; width: 18px; height: 18px; margin-top: 1px; fill: var(--white); }
</style>
</head>
<body>
  <section class="card card--brand">
    <div class="emblem-area" role="img" aria-label="Fingerprint with a handheld magnifying glass"></div>
    <p class="company">Brightwell Evidence Group, LLC</p>
    <p class="motto">veritas aequitas</p>
    <div class="side-strip"><span></span><span></span><span></span></div>
  </section>

  <section class="card card--contact">
    <div class="emblem-area" role="img" aria-label="Fingerprint with a handheld magnifying glass"></div>
    <p class="company">Brightwell Evidence<br>Group, LLC</p>
    <div class="holder">
      <p class="holder-name">Delia Forsythe</p>
      <p class="holder-title">CLPE</p>
    </div>
    <ul class="contact-panel">
      <li><svg viewBox="0 0 24 24"><path d="M6.6 10.8a15 15 0 006.6 6.6l2.2-2.2c.3-.3.7-.4 1-.2 1.1.4 2.3.6 3.6.6.6 0 1 .4 1 1V20c0 .6-.4 1-1 1A17 17 0 013 4c0-.6.4-1 1-1h3.5c.6 0 1 .4 1 1 0 1.3.2 2.5.6 3.6.1.3 0 .7-.2 1z"/></svg>916.428.3071</li>
      <li><svg viewBox="0 0 24 24"><path d="M12 2a7 7 0 00-7 7c0 5 7 13 7 13s7-8 7-13a7 7 0 00-7-7zm0 9.5A2.5 2.5 0 1112 6.5a2.5 2.5 0 010 5z"/></svg>P.O. Box 583172<br>Sacramento, CA 95817</li>
      <li><svg viewBox="0 0 24 24"><path d="M2 5h20v14H2zm2 2v.5l8 5 8-5V7l-8 5z"/></svg>brightwellevidence@mailbox.example</li>
      <li><svg viewBox="0 0 24 24"><path d="M3 4h18v12H3zm2 2v8h14V6zM8 18h8v2H8z"/></svg>brightwellevidencegroup.example</li>
    </ul>
  </section>
</body>
</html>
```